Business Card Design Project

We're an orthopaedic office, and our colors are blue white and balck. Dealing with physicians and healthcare execs, I'd like this card to have a classy, yet overpowering wow factor.

Here are a couple of cards I like that are close to what I'm looking for:
http://www.pixelbazaro.com/design/392047
http://www.pixelbazaro.com/design/286390

Industry/Entity Type

Healthcare

```html
<!DOCTYPE html>
<html lang="en">
<head>
<meta charset="utf-8">
<title>Crestline Orthopaedic &amp; Sports Medicine Center – Business Card</title>
<link rel="stylesheet" href="https://fonts.googleapis.com/css2?family=Source+Sans+3:wght@400;600&display=swap">
<style>
  :root {
    --stage: #2b2b2b;
    --navy: #0b2c5f;
    --navy-deep: #08234d;
    --paper: #ffffff;
    --ink: #1d1d1f;
    --brand-text: #0b2c5f;
  }
  * { margin: 0; padding: 0; box-sizing: border-box; }
  html, body {
    width: 1200px; height: 900px; overflow: hidden;
    background: var(--stage);
    font-family: "Source Sans 3", "Myriad Pro", Arial, sans-serif;
  }
  .stage {
    position: relative; width: 1200px; height: 900px;
  }
  .card {
    position: absolute; top: 308px;
    width: 513px; height: 284px;
    box-shadow: 0 4px 10px rgba(0,0,0,.45);
    overflow: hidden;
  }
  .card--front { left: 73px; background: var(--navy); color: var(--paper); }
  .card--back { left: 616px; background: var(--paper); color: var(--ink); }

  .brand { position: absolute; display: flex; align-items: center; gap: 14px; }
  .brand__mark { display: block; }
  .brand__words { display: flex; flex-direction: column; align-items: flex-end; }
  .brand__name {
    font-weight: 400; letter-spacing: .5px; line-height: 1;
  }
  .brand__tagline {
    font-size: 13px; line-height: 1.05; text-align: right; margin-top: 3px;
  }

  .card--front .brand { left: 118px; top: 116px; }
  .card--front .brand__mark { width: 48px; height: 48px; background: var(--paper); }
  .card--front .brand__name { font-size: 32px; }

  .card--back .brand { left: 30px; top: 34px; gap: 12px; }
  .card--back .brand__mark { width: 40px; height: 40px; background: var(--brand-text); }
  .card--back .brand__name { font-size: 28px; color: var(--brand-text); }
  .card--back .brand__tagline { font-size: 11px; color: var(--ink); }

  .person { position: absolute; left: 45px; top: 158px; }
  .person__name { font-size: 19px; line-height: 1.1; }
  .person__role { font-size: 12px; margin-top: 3px; }

  .contact { position: absolute; left: 45px; top: 216px; list-style: none; }
  .contact__item {
    display: flex; align-items: center; gap: 5px;
    font-size: 13px; line-height: 16px;
  }
  .contact__icon { width: 10px; height: 11px; fill: var(--ink); flex: none; }
</style>
</head>
<body>
<main class="stage">

  <section class="card card--front" aria-label="Card front">
    <div class="brand">
      <span class="brand__mark" aria-hidden="true"></span>
      <div class="brand__words">
        <span class="brand__name">CRESTLINE</span>
        <span class="brand__tagline">Orthopaedic &amp; Sports<br>Medicine Center</span>
      </div>
    </div>
  </section>

  <section class="card card--back" aria-label="Card back">
    <div class="brand">
      <span class="brand__mark" aria-hidden="true"></span>
      <div class="brand__words">
        <span class="brand__name">CRESTLINE</span>
        <span class="brand__tagline">Orthopaedic &amp; Sports<br>Medicine Center</span>
      </div>
    </div>

    <div class="person">
      <p class="person__name">Graham Ellison</p>
      <p class="person__role">CEO</p>
    </div>

    <ul class="contact">
      <li class="contact__item">
        <svg class="contact__icon" viewBox="0 0 10 12" aria-hidden="true"><path d="M5 0a4 4 0 0 0-4 4c0 3 4 8 4 8s4-5 4-8a4 4 0 0 0-4-4zm0 5.6a1.6 1.6 0 1 1 0-3.2 1.6 1.6 0 0 1 0 3.2z"/></svg>
        2180 Larkfield Ave., Riverton, OH 45012
      </li>
      <li class="contact__item">
        <svg class="contact__icon" viewBox="0 0 10 12" aria-hidden="true"><path d="M2.2 0.8l1.6 2.4-1 1c.5 1.6 1.6 3 3 3.9l1-.9 2.3 1.6-.9 1.9C4.6 11 .6 6 1 1.6z"/></svg>
        (555) 214-6730
      </li>
      <li class="contact__item">
        <svg class="contact__icon" viewBox="0 0 10 12" aria-hidden="true"><path d="M0 3h10v6H0z M0 3l5 3.5L10 3" stroke="#fff" stroke-width=".7"/></svg>
        gellison@crestlineortho.com
      </li>
    </ul>
  </section>

</main>
</body>
</html>
```